Personal Training Business Card Design

I have just started my own personal training business called "Lena Brookfield Fitness". My goal as a personal trainer is to motivate, inspire and educate all of my clients about the benefits of regular exercise, nourishing the body with nutritious foods and living healthy. I train both men and women, so I would like a business card that will appeal to both sexes and not come across too feminine or too masculine. I'm looking for a fresh, yet simple look which uses "fresh" colours such as green, white and grey - similar to my logo (but open to other effective gender-neutral colour schemes). I am open to using the logo I have uploaded as one image together, or separating the text and image (also supplied).
Industry/Entity Type
Personal Trainer
Contact Information for Business Card
Lena Brookfield
Fitness Coach
Address: Ground Floor, Quillmore House, 48 Harlow St, Brisbane City, 4000
Email: lenabrookfieldfitness@mailora.example
Phone: 0455 392 647
Facebook: www.socialnook.example/lenabrookfieldfitness
Look and feel

```html
<!DOCTYPE html>
<html lang="en">
<head>
<meta charset="utf-8">
<title>Lena Brookfield Fitness – Business Card</title>
<link rel="stylesheet" href="https://fonts.googleapis.com/css2?family=Comfortaa:wght@300;400&family=Raleway:wght@300;400&display=swap">
<style>
  :root {
    --green: #8cc63f;
    --green-dark: #7ab52f;
    --white: #ffffff;
    --grey: #6f6f6f;
    --grey-light: #8a8a8a;
    --link-blue: #4a7fc1;
    --stage: #3d3d3d;
  }
  * { margin: 0; padding: 0; box-sizing: border-box; }
  html, body {
    width: 1200px;
    height: 900px;
    overflow: hidden;
    background: var(--stage);
  }
  .stage {
    position: relative;
    width: 1200px;
    height: 900px;
  }
  .card {
    position: absolute;
    left: 260px;
    width: 680px;
    height: 388px;
    border-radius: 26px;
    overflow: hidden;
  }

  /* Front */
  .card--front {
    top: 44px;
    background: var(--green);
  }
  .front__mark {
    position: absolute;
    left: 72px;
    top: 124px;
    width: 140px;
    height: 140px;
    background: var(--white);
  }
  .front__wordmark {
    position: absolute;
    left: 248px;
    top: 160px;
    font-family: 'Raleway', sans-serif;
    font-weight: 400;
    font-size: 27px;
    letter-spacing: 0.5px;
    color: var(--white);
    text-transform: uppercase;
    white-space: nowrap;
  }
  .front__tagline {
    position: absolute;
    left: 250px;
    top: 198px;
    font-family: 'Comfortaa', sans-serif;
    font-size: 19px;
    color: var(--grey);
    white-space: nowrap;
  }

  /* Back */
  .card--back {
    top: 468px;
    background: var(--white);
  }
  .back__name {
    position: absolute;
    left: 48px;
    top: 46px;
    font-family: 'Comfortaa', sans-serif;
    font-weight: 400;
    font-size: 32px;
    color: var(--green);
  }
  .back__role {
    position: absolute;
    left: 50px;
    top: 90px;
    font-family: 'Comfortaa', sans-serif;
    font-size: 13px;
    letter-spacing: 3px;
    color: var(--grey);
    text-transform: uppercase;
  }
  .back__contact {
    position: absolute;
    left: 50px;
    top: 138px;
    font-family: 'Comfortaa', sans-serif;
    font-size: 12.5px;
    line-height: 19px;
    color: var(--grey);
    list-style: none;
  }
  .back__contact .gap { margin-top: 14px; }

  .back__brand {
    position: absolute;
    right: 40px;
    top: 40px;
    width: 300px;
    text-align: center;
  }
  .back__brand-mark {
    display: block;
    margin: 0 auto 10px;
  }
  .back__wordmark {
    font-family: 'Raleway', sans-serif;
    font-weight: 400;
    font-size: 19px;
    color: var(--green);
    text-transform: uppercase;
    letter-spacing: 0.5px;
    white-space: nowrap;
  }
  .back__tagline {
    font-family: 'Comfortaa', sans-serif;
    font-size: 17px;
    color: var(--grey);
    white-space: nowrap;
  }

  .back__social {
    position: absolute;
    right: 30px;
    bottom: 34px;
    display: flex;
    align-items: center;
    gap: 12px;
  }
  .back__url {
    font-family: 'Comfortaa', sans-serif;
    font-size: 13px;
    color: var(--link-blue);
    white-space: nowrap;
  }
  .back__social-square {
    width: 30px;
    height: 30px;
    background: var(--link-blue);
    border-radius: 4px;
  }
</style>
</head>
<body>
  <main class="stage">
    <section class="card card--front" aria-label="Business card front">
      <div class="front__mark"></div>
      <h1 class="front__wordmark">Lena Brookfield Fitness</h1>
      <p class="front__tagline">motivate. inspire. educate.</p>
    </section>

    <section class="card card--back" aria-label="Business card back">
      <h2 class="back__name">Lena Brookfield</h2>
      <p class="back__role">Fitness Coach</p>
      <ul class="back__contact">
        <li>0455 392 647</li>
        <li>lenabrookfieldfitness@mailora.example</li>
        <li class="gap">Ground Floor, Quillmore House,</li>
        <li>48 Harlow St, Brisbane City, 4000</li>
      </ul>

      <div class="back__brand">
        <svg class="back__brand-mark" width="120" height="120" viewBox="0 0 120 120" aria-hidden="true">
          <circle cx="60" cy="60" r="60" fill="var(--green)"/>
        </svg>
        <p class="back__wordmark">Lena Brookfield Fitness</p>
        <p class="back__tagline">motivate. inspire. educate.</p>
      </div>

      <div class="back__social">
        <span class="back__url">www.socialnook.example/lenabrookfieldfitness</span>
        <span class="back__social-square"></span>
      </div>
    </section>
  </main>
</body>
</html>
```